Business card and stationary for accounting firm
Business card and stationary
Business card and stationary for accounting firm - Financial Services
Creative Brief
Simple
Daniel Brennick
28340 Wexley Parkway Ste 210 Irvine, Ca. 92604
dbrennick@brennickcpa-example.com
brennickcpa-example.com
Looking for simple and professional design for my accounting firm. I also need jpg or other files for header and footers in word for pdf and online printing. Most documents I send would be emailed. Also looking for signature on email messages too.
Not sure but like it simple with maybe my logo and website address.

```html
<!DOCTYPE html>
<html lang="en">
<head>
<meta charset="utf-8">
<title>Brennick CPA Group – Business Card</title>
<link href="https://fonts.googleapis.com/css2?family=Cinzel:wght@400;600&family=Lato:wght@400;700&display=swap" rel="stylesheet">
<style>
  :root {
    --navy: #2b3566;
    --navy-deep: #232b55;
    --ink: #1d1f2a;
    --grey: #8a8c94;
    --paper: #ffffff;
    --stage: #e9eaee;
    --rule: #c9cad0;
  }
  * { box-sizing: border-box; margin: 0; padding: 0; }
  html, body { width: 1200px; height: 864px; overflow: hidden; }
  body { background: var(--stage); position: relative; font-family: "Lato", Arial, sans-serif; }

  .card {
    position: absolute;
    width: 640px;
    height: 366px;
    border-radius: 26px;
    overflow: hidden;
    box-shadow: 0 10px 28px rgba(20, 24, 45, 0.22);
  }

  /* Front: navy face */
  .card-front {
    left: 70px; top: 70px;
    background: linear-gradient(160deg, var(--navy) 0%, var(--navy-deep) 100%);
    color: var(--paper);
  }
  .front-mark {
    position: absolute; left: 0; right: 0; top: 140px;
    display: flex; align-items: center; justify-content: center; gap: 16px;
  }
  .front-mark .mark-square { width: 22px; height: 22px; background: var(--paper); }
  .front-mark .mark-name {
    font-family: "Cinzel", Georgia, serif; font-weight: 600;
    font-size: 30px; letter-spacing: 4px; color: var(--paper);
  }
  .front-web {
    position: absolute; left: 0; right: 0; bottom: 46px; text-align: center;
    font-size: 12px; letter-spacing: 7px; text-transform: uppercase; color: #d7dbeb;
  }

  /* Back: white face */
  .card-back {
    left: 490px; top: 420px;
    background: var(--paper);
    color: var(--navy);
  }
  .firm {
    position: absolute; right: 44px; top: 46px; text-align: right;
  }
  .firm-name {
    display: flex; align-items: center; justify-content: flex-end; gap: 12px;
    font-family: "Cinzel", Georgia, serif; font-weight: 600;
    font-size: 34px; letter-spacing: 2px; color: var(--navy);
  }
  .firm-name .mark-square { width: 20px; height: 20px; background: var(--navy); }
  .firm-tagline {
    margin-top: 4px; font-family: "Cinzel", Georgia, serif;
    font-size: 10px; letter-spacing: 2.4px; color: var(--grey);
  }
  .person {
    position: absolute; left: 44px; top: 168px;
    display: flex; align-items: stretch; gap: 18px;
  }
  .person-name {
    align-self: center;
    font-family: "Cinzel", Georgia, serif; font-weight: 600;
    font-size: 17px; letter-spacing: 1.5px; color: var(--navy);
  }
  .divider { width: 1px; background: var(--rule); }
  .contact { list-style: none; display: flex; flex-direction: column; gap: 6px; }
  .contact li {
    display: flex; align-items: center; gap: 8px;
    font-size: 11px; color: var(--ink); letter-spacing: 0.3px;
  }
  .contact .dot {
    width: 12px; height: 12px; border-radius: 50%; background: var(--navy); flex: none;
  }
  .contact .plain { padding-left: 20px; }
  .swoosh { position: absolute; left: 0; bottom: 0; width: 640px; height: 140px; }
</style>
</head>
<body>

  <section class="card card-front" aria-label="Business card front">
    <div class="front-mark">
      <span class="mark-square"></span>
      <span class="mark-name">BRENNICK CPA</span>
    </div>
    <p class="front-web">www.brennickcpa-example.com</p>
  </section>

  <section class="card card-back" aria-label="Business card back">
    <div class="firm">
      <h1 class="firm-name"><span class="mark-square"></span>BRENNICK CPA GROUP</h1>
      <p class="firm-tagline">CERTIFIED PUBLIC ACCOUNTANCY CORPORATION</p>
    </div>

    <div class="person">
      <p class="person-name">DANIEL BRENNICK</p>
      <span class="divider"></span>
      <ul class="contact">
        <li><span class="dot"></span>28340 Wexley Parkway Ste 210</li>
        <li class="plain">Irvine, Ca. 92604</li>
        <li><span class="dot"></span>dbrennick@brennickcpa-example.com</li>
        <li><span class="dot"></span>www.brennickcpa-example.com</li>
      </ul>
    </div>

    <svg class="swoosh" viewBox="0 0 640 140" preserveAspectRatio="none" aria-hidden="true">
      <path d="M0 120 C 200 130, 420 110, 640 20 L640 60 C 440 130, 220 140, 0 140 Z" fill="#1d1f2a"/>
      <path d="M0 132 C 220 138, 440 125, 640 60 L640 140 L0 140 Z" fill="#2b3566"/>
      <path d="M0 116 C 220 126, 430 104, 640 6" fill="none" stroke="#c9cad0" stroke-width="2"/>
    </svg>
  </section>

</body>
</html>
```